Vextor Promo Consulting Company Website

Need a website for a consulting company that will help nonprofits qualify to get free online ads from Vextor in their Vextor Promo Fund program and that will also help them manage the ad spend. Need a new logo as part of this. You can look at our current site at www.fundharborly.example to get a sense as to content. I am looking for a nice looking site that will be easy to maintain and expand upon. It should load fast and be good design from an SEO perspective.

Target Market(s)

Midsized nonprofits.

Industry/Entity Type

nonprofit marketing

Coding

Coded - Design and coding required

Number of Pages Required

5+ page

```html
<!DOCTYPE html>
<html lang="en">
<head>
<meta charset="utf-8">
<title>Information Center – Fund Harborly</title>
<link rel="stylesheet" href="https://fonts.googleapis.com/css2?family=Nunito+Sans:wght@400;600;700;800;900&display=swap">
<style>
:root{
  --blue:#3a59a8;
  --hero:#5c79bb;
  --hero-soft:#7890c8;
  --orange:#f5892d;
  --ink:#1c1c1c;
  --white:#ffffff;
  --cta-dark:#3b342e;
  --wave-light:#d9e0f1;
}
*{margin:0;padding:0;box-sizing:border-box}
html,body{width:726px;height:1200px;overflow:hidden;background:var(--white)}
body{position:relative;font-family:"Nunito Sans",sans-serif;color:var(--ink)}

/* header */
.site-header{position:absolute;left:0;top:0;width:726px;height:59px;background:var(--white)}
.brand{position:absolute;left:98px;top:13px;display:flex;align-items:center;gap:6px}
.brand-mark{width:32px;height:32px;border:3px solid var(--blue);border-radius:50%}
.brand-name{font-weight:800;font-size:15px;letter-spacing:.6px;color:var(--blue)}
.main-nav{position:absolute;top:23px;left:393px;display:flex;gap:20px;font-size:10px}
.main-nav a{color:var(--ink);text-decoration:none}
.main-nav a.active{color:var(--orange)}

/* hero */
.hero{position:absolute;left:0;top:59px;width:726px;height:227px;background:var(--hero);overflow:hidden}
.hero-circle{position:absolute;left:370px;top:-120px;width:520px;height:480px;border-radius:50%;background:var(--hero-soft)}
.hero-title{position:absolute;left:98px;top:82px;font-size:25px;line-height:28px;font-weight:800;color:var(--white)}
.hero-art{position:absolute;left:340px;top:24px;width:318px;height:180px;
  background:
    radial-gradient(ellipse 30% 35% at 50% 62%,rgba(245,137,45,.95),rgba(245,137,45,0) 100%),
    radial-gradient(ellipse 55% 50% at 45% 60%,rgba(205,222,245,.85),rgba(205,222,245,0) 100%),
    radial-gradient(ellipse 40% 30% at 55% 25%,rgba(235,242,252,.6),rgba(235,242,252,0) 100%);
}
.hero-ground{position:absolute;left:340px;top:203px;width:318px;height:1.5px;background:#2b3f78}

.breadcrumb{position:absolute;left:98px;top:296px;font-size:11px}
.breadcrumb b{color:var(--orange);font-weight:800}

/* posts */
.post{position:absolute;top:331px;width:170px}
.post-thumb{width:170px;height:191px;border-radius:5px}
.thumb-team{background:
  radial-gradient(ellipse 40% 45% at 70% 55%,rgba(120,105,95,.8),rgba(120,105,95,0)),
  radial-gradient(ellipse 35% 40% at 15% 60%,rgba(60,80,120,.8),rgba(60,80,120,0)),
  linear-gradient(180deg,#eef0f0 0%,#c9ced2 45%,#5b5e63 100%)}
.thumb-faq{background:
  radial-gradient(ellipse 60% 35% at 55% 30%,#ffffff,rgba(255,255,255,0)),
  linear-gradient(160deg,#f6eef1 0%,#ebe9ec 45%,#6c6c70 75%,#e8cbc0 100%)}
.thumb-approve{background:
  radial-gradient(ellipse 35% 35% at 65% 50%,rgba(240,240,240,.9),rgba(240,240,240,0)),
  linear-gradient(160deg,#56c6d4,#4fbccb)}
.post-date{margin-top:12px;font-size:8.5px;color:var(--orange);display:flex;align-items:center;gap:5px}
.post-title{margin-top:6px;font-size:10.8px;line-height:15px;font-weight:800;letter-spacing:.8px;text-transform:uppercase;padding-left:1px}
.btn{display:inline-block;border-radius:12px;font-size:8.5px;letter-spacing:.3px;text-transform:uppercase;color:var(--white);text-decoration:none}
.btn-read{margin-top:5px;width:82px;height:20px;line-height:20px;text-align:center;background:var(--blue)}

/* cta */
.cta{position:absolute;left:0;top:675px;width:726px;height:330px;background:
  radial-gradient(ellipse 35% 40% at 85% 25%,rgba(200,200,205,.55),rgba(200,200,205,0)),
  radial-gradient(ellipse 30% 30% at 90% 85%,rgba(160,130,95,.6),rgba(160,130,95,0)),
  linear-gradient(120deg,#4d4036,var(--cta-dark) 50%,#6d645c)}
.cta-title{position:absolute;left:98px;top:72px;font-size:30px;line-height:38px;font-weight:900;letter-spacing:1.5px;color:var(--white)}
.btn-contact{position:absolute;left:98px;top:158px;width:118px;height:24px;line-height:24px;text-align:center;background:var(--orange);font-size:9px;border-radius:13px}

/* footer */
.footer-wave{position:absolute;left:0;top:930px;width:726px;height:270px}
.footer-brand{position:absolute;left:239px;top:987px;display:flex;align-items:center;gap:9px}
.footer-brand .brand-mark{width:46px;height:46px;border-color:var(--white)}
.footer-brand .brand-name{font-size:22px;color:var(--white);letter-spacing:1.2px}
.footer-nav{position:absolute;top:1059px;left:212px;display:flex;gap:43px;font-size:9.5px}
.footer-nav a{color:var(--white);text-decoration:none}
.rule{position:absolute;left:98px;width:531px;height:1px;background:rgba(255,255,255,.18)}
.contact-item{position:absolute;top:1114px;display:flex;align-items:center;gap:8px;color:var(--white);font-size:10px}
.contact-item b{font-weight:700}
.contact-sep{position:absolute;left:333px;top:1113px;width:1px;height:29px;background:rgba(0,0,0,.3)}
.copyright{position:absolute;left:98px;top:1178px;font-size:8px;color:var(--white)}
.social{position:absolute;top:1173px;width:18px;height:18px;border:1px solid var(--white);border-radius:50%}
</style>
</head>
<body>

<header class="site-header">
  <div class="brand"><span class="brand-mark"></span><span class="brand-name">FUND HARBORLY</span></div>
  <nav class="main-nav">
    <a href="#">Home</a><a href="#">Services</a><a href="#" class="active">Information Center</a><a href="#">Contact</a>
  </nav>
</header>

<section class="hero">
  <div class="hero-circle"></div>
  <h1 class="hero-title">Information<br>Center</h1>
  <div class="hero-art" role="img" aria-label="Illustration of a team with a large orange megaphone in front of a laptop and city skyline"></div>
</section>
<div class="hero-ground"></div>

<div class="breadcrumb">Home / <b>Information Center</b></div>

<article class="post" style="left:98px">
  <div class="post-thumb thumb-team" role="img" aria-label="Photo of a team discussing in a bright office"></div>
  <div class="post-date"><svg width="9" height="9" viewBox="0 0 9 9"><rect x=".5" y="1.5" width="8" height="7" rx="1" fill="none" stroke="#f5892d"/><line x1=".5" y1="3.5" x2="8.5" y2="3.5" stroke="#f5892d"/></svg>September 28, 2021</div>
  <h2 class="post-title">Ongoing Eligibility Requirements</h2>
  <a class="btn btn-read" href="#">Read More</a>
</article>

<article class="post" style="left:278px">
  <div class="post-thumb thumb-faq" role="img" aria-label="Photo of hands typing on a laptop showing a help and FAQ screen"></div>
  <div class="post-date"><svg width="9" height="9" viewBox="0 0 9 9"><rect x=".5" y="1.5" width="8" height="7" rx="1" fill="none" stroke="#f5892d"/><line x1=".5" y1="3.5" x2="8.5" y2="3.5" stroke="#f5892d"/></svg>September 28, 2021</div>
  <h2 class="post-title">Frequently Asked Questions on Vextor Promo Fund</h2>
  <a class="btn btn-read" href="#">Read More</a>
</article>

<article class="post" style="left:459px">
  <div class="post-thumb thumb-approve" role="img" aria-label="Illustration of an approval stamp on documents beside a phone"></div>
  <div class="post-date"><svg width="9" height="9" viewBox="0 0 9 9"><rect x=".5" y="1.5" width="8" height="7" rx="1" fill="none" stroke="#f5892d"/><line x1=".5" y1="3.5" x2="8.5" y2="3.5" stroke="#f5892d"/></svg>September 14, 2021</div>
  <h2 class="post-title">What are Vextor Promo?</h2>
  <a class="btn btn-read" href="#">Read More</a>
</article>

<section class="cta" role="img" aria-label="Photo of colleagues joining fists over a desk with papers and a laptop">
  <h2 class="cta-title">LETS GET<br>STARTED TODAY?</h2>
  <a class="btn btn-contact" href="#">Contact Us Today</a>
</section>

<footer>
  <svg class="footer-wave" viewBox="0 0 726 270" preserveAspectRatio="none">
    <path d="M0 35 Q363 -30 726 40 L726 270 L0 270Z" fill="var(--wave-light)"/>
    <path d="M0 70 Q363 -20 726 70 L726 270 L0 270Z" fill="var(--blue)"/>
  </svg>
  <div class="footer-brand"><span class="brand-mark"></span><span class="brand-name">FUND HARBORLY</span></div>
  <nav class="footer-nav">
    <a href="#">Home</a><a href="#">Services</a><a href="#">Information Center</a><a href="#">Contact</a>
  </nav>
  <div class="rule" style="top:1093px"></div>
  <div class="contact-item" style="left:170px">
    <svg width="20" height="20" viewBox="0 0 20 20"><circle cx="10" cy="10" r="9" fill="none" stroke="#f5892d"/><path d="M6 5.5l2 -.5 1 3-1.3 1a6 6 0 0 0 3.3 3.3l1-1.3 3 1-.5 2C10 15 5 10 6 5.5z" fill="none" stroke="#f5892d"/></svg>
    <span><b>Call Us:</b> (555) 014-2290</span>
  </div>
  <div class="contact-sep"></div>
  <div class="contact-item" style="left:362px">
    <svg width="24" height="20" viewBox="0 0 24 20"><rect x="8" y="5" width="14" height="10" fill="none" stroke="#f5892d"/><path d="M8 5l7 6 7-6" fill="none" stroke="#f5892d"/><path d="M1 8h5M3 11h4M1 14h5" stroke="#f5892d"/></svg>
    <span><b>Email Us:</b> info@fundharborly.example</span>
  </div>
  <div class="rule" style="top:1163px"></div>
  <p class="copyright">Copyright © 2021 FUND HARBORLY. All Rights Reserved.</p>
  <span class="social" style="left:588px"></span>
  <span class="social" style="left:611px"></span>
</footer>

</body>
</html>
```